Harborline Wonder Evenings - A magic website for a monthly modern magic show

Looking to build a website to promote my new monthly magic show

Sites like this. https://loftwanderer-example.com/ https://sevenunlikelywondersrevue-example.com/

Target Market(s)

18-65 year old men and women who enjoy live entertainment especially magic

Industry/Entity Type

Entertainment

Coding

Coded - Design and coding required

Number of Pages Required

3 page

Colors

Designer to choose colors to be used in the design.

Requirements
Must have
• Wanting a wordpress site.
• Contact form, media section for photos and videos to be posted.
• A “reviews/testimonials” section.

```html
<!DOCTYPE html>
<html lang="en">
<head>
<meta charset="utf-8">
<title>Harborline Wonder Evenings</title>
<link rel="stylesheet" href="https://fonts.googleapis.com/css2?family=Cinzel:wght@400;500&family=Poppins:wght@300;400;500;700&display=swap">
<style>
:root{
  --bg:#0c0c0c;
  --bg-soft:#151515;
  --gold:#c8a565;
  --gold-dark:#8a6a34;
  --text:#e9e6e0;
  --muted:#9c9890;
  --slate:#2a2e33;
  --wine:#4a1616;
  --navy:#1c1f3c;
  --field:#1b1b1b;
  --line:#444;
}
*{margin:0;padding:0;box-sizing:border-box}
html,body{width:1200px;height:4584px;overflow:hidden}
body{background:var(--bg);color:var(--text);font-family:"Poppins",sans-serif;position:relative}
.abs{position:absolute}
.serif{font-family:"Cinzel",serif;font-weight:400;letter-spacing:2px}
.gold{color:var(--gold)}
.para{font-size:13px;line-height:22px;color:var(--muted)}
.btn{position:absolute;background:linear-gradient(180deg,#c9a76a,#8f6d37);color:#1a1208;font-size:12px;font-weight:500;text-align:center;line-height:36px;height:36px;width:152px;border-radius:3px}
/* header */
.logo-name{font-weight:700;font-size:32px;color:#fff;line-height:34px}
.logo-tag{font-size:11px;color:var(--muted);letter-spacing:1px}
.nav{top:30px;left:420px;display:flex;gap:34px;font-size:13px;color:var(--text)}
.social{display:flex;gap:10px}
.social span{width:22px;height:22px;border-radius:50%;background:#e0e0e0;display:block}
/* hero */
.hero-art{left:700px;top:0;width:500px;height:780px;background:radial-gradient(ellipse at 50% 40%,rgba(180,180,180,.28),rgba(12,12,12,0) 65%)}
.hero-title{left:152px;top:300px;font-size:68px;letter-spacing:6px;color:#ddd}
.scroll{left:560px;top:620px;width:80px;text-align:center;font-size:11px;color:var(--muted)}
/* brush panels */
.brush{position:absolute}
.photo{position:absolute}
.section-title{font-size:48px;letter-spacing:4px;color:#eee}
.sub{font-size:15px;font-weight:500;color:var(--gold);letter-spacing:.5px}
/* carousel */
.thumb{position:absolute;top:2860px;height:252px}
.play{position:absolute;left:50%;top:50%;width:56px;height:56px;margin:-28px 0 0 -28px;border-radius:50%;background:#fff}
.play:after{content:"";position:absolute;left:22px;top:17px;border-left:18px solid #222;border-top:11px solid transparent;border-bottom:11px solid transparent}
.arrow{position:absolute;font-size:30px;color:#ddd}
/* footer */
.foot-head{font-size:14px;font-weight:500;color:var(--gold);letter-spacing:1px}
.foot-list{font-size:13px;line-height:24px;color:var(--muted);list-style:none}
.field{position:absolute;background:var(--field);border:1px solid var(--line);font-size:11px;color:var(--muted);padding:6px 10px}
</style>
</head>
<body>

<!-- Header -->
<header>
  <div class="abs" style="left:152px;top:16px">
    <div class="logo-name">Harborline</div>
    <div class="logo-tag">Wonder Evenings</div>
  </div>
  <nav class="abs nav"><span>Home</span><span>About</span><span>Gallery</span><span>FAQ</span><span>Tickets Online</span></nav>
  <div class="abs social" style="left:996px;top:26px"><span></span><span></span></div>
</header>

<!-- Hero -->
<section class="hero">
  <div class="abs hero-art" role="img" aria-label="Drifting white smoke on black"></div>
  <h1 class="abs serif hero-title"><span class="gold">UNFOR</span>GETTABLE</h1>
  <p class="abs para" style="left:152px;top:398px;width:520px">Step into an evening where the impossible feels close enough to touch. Live modern magic, once a month, in an intimate harborside room made for wonder and delight.</p>
  <div class="btn" style="left:152px;top:496px">Book Tickets</div>
  <div class="abs scroll">
    <svg width="20" height="44" viewBox="0 0 20 44"><path d="M10 0V40M3 33l7 8 7-8" stroke="#ddd" stroke-width="2" fill="none"/></svg>
    <div style="margin-top:12px">Scroll Down</div>
  </div>
</section>

<!-- About -->
<section class="about">
  <svg class="brush" style="left:150px;top:820px" width="1050" height="560" viewBox="0 0 1050 560"><path d="M30 40 L1020 0 L1040 120 L1010 300 L1050 420 L960 540 L80 560 L20 460 L0 300 L40 160 Z" fill="var(--slate)" opacity=".75"/></svg>
  <div class="photo" style="left:640px;top:820px;width:400px;height:500px;background:linear-gradient(160deg,#3a4048,#1c1f24)" role="img" aria-label="Magician in a blazer fanning playing cards"></div>
  <div class="photo" style="left:960px;top:800px;width:160px;height:200px;transform:rotate(28deg);background:linear-gradient(135deg,#f3f0ea,#cfcac0);border-radius:8px" role="img" aria-label="Flying playing card"></div>
  <h2 class="abs serif section-title" style="left:292px;top:1000px"><span class="gold">ABO</span>UT US</h2>
  <div class="abs sub" style="left:292px;top:1104px">Where Modern Magic Comes Alive</div>
  <p class="abs para" style="left:292px;top:1140px;width:470px">Every month we open our doors for a night of close-up wonders, clever illusions and real laughter. Our performers blend classic sleight of hand with fresh ideas, so each show feels new. Seats are limited and every guest is close to the action, so you will see every card, coin and surprise from just a few steps away.</p>
</section>

<!-- Feature -->
<section class="feature">
  <svg class="brush" style="left:0;top:1680px" width="1200" height="560" viewBox="0 0 1200 560"><path d="M0 30 L1150 0 L1190 140 L1160 330 L1200 480 L1100 560 L60 540 L0 420 Z" fill="var(--wine)" opacity=".8"/></svg>
  <div class="photo" style="left:140px;top:1760px;width:420px;height:480px;background:radial-gradient(ellipse at 50% 60%,#6a3a2a,#2a1010 70%)" role="img" aria-label="Open hand tossing dice into the air"></div>
  <h2 class="abs serif section-title" style="left:524px;top:1850px"><span class="gold">HARBOR</span>LINE MAGIC</h2>
  <div class="abs sub" style="left:524px;top:1950px">IS AN INTERACTIVE MAGIC EXPERIENCE</div>
  <p class="abs para" style="left:524px;top:1984px;width:470px">You are not just watching the show, you are part of it. Guests pick the cards, hold the props and help shape the night, making every evening one of a kind.</p>
  <div class="btn" style="left:524px;top:2106px">Book Tickets</div>
  <div class="photo" style="left:20px;top:2290px;width:170px;height:230px;transform:rotate(-32deg);background:linear-gradient(135deg,#f2efe8,#bdb8ae);border-radius:8px" role="img" aria-label="Tumbling playing card"></div>
</section>

<!-- Media -->
<section class="media">
  <h2 class="abs serif section-title" style="left:280px;top:2586px"><span class="gold">PHOTOS</span> &amp; VIDEOS</h2>
  <div class="abs sub" style="left:292px;top:2686px;color:#eee">MEET THE MAGICIAN</div>
  <p class="abs para" style="left:292px;top:2720px;width:470px">Take a look behind the curtain with clips and photos from recent shows, rehearsals and the people who make the magic.</p>
  <span class="arrow" style="left:58px;top:2962px">&#8249;</span>
  <div class="thumb" style="left:148px;width:272px;background:linear-gradient(160deg,#4a4a4a,#181818)" role="img" aria-label="Hand holding a card in smoke"></div>
  <div class="thumb" style="left:460px;width:280px;background:linear-gradient(160deg,#3d5a78,#1a2230)" role="img" aria-label="Performer in a hood, video"><span class="play"></span></div>
  <div class="thumb" style="left:780px;width:272px;background:linear-gradient(160deg,#4c4c4c,#1a1a1a)" role="img" aria-label="Magician on stage, video"><span class="play"></span></div>
  <span class="arrow" style="left:1118px;top:2962px">&#8250;</span>
  <div class="btn" style="left:524px;top:3174px">View Gallery</div>
</section>

<!-- Testimonials -->
<section class="reviews">
  <svg class="brush" style="left:0;top:3360px" width="1200" height="580" viewBox="0 0 1200 580"><path d="M0 40 L1180 0 L1200 160 L1170 360 L1200 500 L1080 580 L40 560 L0 430 Z" fill="var(--navy)" opacity=".85"/></svg>
  <h2 class="abs serif section-title" style="left:280px;top:3570px"><span class="gold">CLIENTS</span> TESTIMONIALS</h2>
  <div class="photo" style="left:292px;top:3700px;width:208px;height:200px;background:linear-gradient(160deg,#8a8f96,#3c4148)" role="img" aria-label="Portrait of a reviewer"></div>
  <div class="abs" style="left:524px;top:3732px;font-size:14px;font-weight:500;color:var(--gold)">MARCUS BELL <span style="color:var(--muted);font-weight:400">| Guest</span></div>
  <p class="abs para" style="left:524px;top:3764px;width:470px">An incredible night out. The tricks happened inches from my face and I still cannot explain a single one. Warm crowd, great host, we are already booked for next month.</p>
  <span class="arrow" style="left:524px;top:3850px;font-size:26px">&#8249;</span>
  <span class="arrow" style="left:588px;top:3850px;font-size:26px">&#8250;</span>
</section>

<!-- Footer -->
<footer>
  <div class="abs" style="left:188px;top:4212px">
    <div class="logo-name">Harborline</div>
    <div class="logo-tag">Wonder Evenings</div>
  </div>
  <ul class="abs foot-list" style="left:188px;top:4284px"><li>Pier Nine Hall</li><li>48 Lantern Quay</li><li>Harbor City, HC 20417</li></ul>
  <div class="abs social" style="left:188px;top:4380px"><span style="background:var(--gold)"></span><span style="background:var(--gold)"></span></div>
  <div class="abs foot-head" style="left:428px;top:4220px">QUICK LINKS</div>
  <ul class="abs foot-list" style="left:428px;top:4266px"><li>Home</li><li>About</li><li>Gallery</li><li>FAQ</li><li>Tickets</li><li>Contact</li></ul>
  <div class="abs foot-head" style="left:744px;top:4220px">GET IN TOUCH</div>
  <div class="field" style="left:744px;top:4278px;width:128px;height:28px">Name</div>
  <div class="field" style="left:880px;top:4278px;width:132px;height:28px">Email</div>
  <div class="field" style="left:744px;top:4314px;width:128px;height:28px">Phone No.</div>
  <div class="field" style="left:744px;top:4350px;width:268px;height:96px">Message</div>
  <div class="btn" style="left:744px;top:4460px;width:88px;height:28px;line-height:28px">Submit</div>
  <div class="abs" style="left:188px;top:4514px;font-size:11px;color:var(--muted)">Harborline Wonder Evenings Copyright © 2024</div>
</footer>

</body>
</html>
```